KRT business cards

I need a Business card design for my self. I am behavior analyst owner of a new company based in Miami. We offer Applied Behavior Analysis (ABA) services to individuals with developmental disabilities.

Business

```html
<!DOCTYPE html>
<html lang="en">
<head>
<meta charset="utf-8">
<title>KRT Business Cards</title>
<link rel="stylesheet" href="https://fonts.googleapis.com/css2?family=Crimson+Text:wght@400;600;700&display=swap">
<style>
  :root {
    --bg: #d5d6d8;
    --white: #ffffff;
    --navy: #2c5282;
    --navy-deep: #28497a;
    --green: #5aa24a;
    --leaf-tint: #5b7eaa;
    --ink-light: #ffffff;
  }
  * { margin: 0; padding: 0; box-sizing: border-box; }
  html, body { width: 1200px; height: 1000px; overflow: hidden; }
  body {
    position: relative;
    background: var(--bg);
    font-family: "Crimson Text", Georgia, serif;
  }
  .card {
    position: absolute;
    width: 710px;
    height: 420px;
    overflow: hidden;
    background: var(--white);
  }
  /* Front card */
  .card--front { left: 85px; top: 45px; }
  .front__brand-panel {
    position: absolute; left: 0; top: 0;
    width: 305px; height: 100%;
    display: flex; flex-direction: column;
    align-items: center; justify-content: center; gap: 14px;
  }
  .brand-dot {
    width: 90px; height: 90px; border-radius: 50%;
    background: var(--green);
  }
  .brand-name {
    color: var(--navy);
    font-weight: 600;
    font-size: 31px;
    text-align: center;
    line-height: 1.05;
  }
  .front__divider {
    position: absolute; left: 305px; top: 0;
    width: 9px; height: 100%; background: var(--green);
  }
  .front__services-panel {
    position: absolute; left: 314px; top: 0; right: 0; bottom: 0;
    background: var(--navy);
  }
  .service-list {
    list-style: none;
    position: absolute; left: 36px; top: 48px;
    color: var(--ink-light);
    font-size: 29px;
  }
  .service-list li {
    display: flex; align-items: center; gap: 14px;
    height: 64px;
  }
  .service-list li::before {
    content: ""; width: 12px; height: 12px; border-radius: 50%;
    background: var(--ink-light);
    flex: none;
  }
  .leaf-decor {
    position: absolute; right: 0; bottom: 0;
    width: 170px; height: 190px;
    background: radial-gradient(ellipse at 80% 80%, var(--leaf-tint) 0%, rgba(91,126,170,0.35) 55%, rgba(91,126,170,0) 75%);
  }
  /* Back card */
  .card--back { left: 440px; top: 520px; }
  .back__waves { position: absolute; inset: 0; }
  .back__mark {
    position: absolute; left: 0; right: 0; top: 70px;
    display: flex; flex-direction: column; align-items: center; gap: 10px;
  }
  .brand-dot--small { width: 70px; height: 70px; }
  .back__initials {
    color: var(--navy);
    font-weight: 700;
    font-size: 52px;
    letter-spacing: 2px;
    line-height: 1;
  }
  .holder {
    position: absolute; left: 50px; top: 305px;
    color: var(--ink-light);
  }
  .holder__name {
    font-weight: 700; font-size: 21px; letter-spacing: 0.5px;
    margin-bottom: 4px;
  }
  .holder__title { font-size: 18px; line-height: 1.15; }
  .contact {
    list-style: none;
    position: absolute; left: 395px; top: 290px;
    color: var(--ink-light);
    font-size: 23px;
  }
  .contact li { display: flex; align-items: center; gap: 12px; height: 32px; }
  .contact svg { width: 20px; height: 20px; flex: none; }
</style>
</head>
<body>

<section class="card card--front" aria-label="Business card front">
  <div class="front__brand-panel">
    <span class="brand-dot" aria-hidden="true"></span>
    <p class="brand-name">Kind Roots Therapy</p>
  </div>
  <div class="front__divider"></div>
  <div class="front__services-panel">
    <ul class="service-list">
      <li>Applied Behavior Analysis</li>
      <li>Parent/Teacher Training</li>
      <li>Social Skills Training</li>
      <li>Tutoring</li>
    </ul>
    <div class="leaf-decor" role="img" aria-label="Faint leaf decoration"></div>
  </div>
</section>

<section class="card card--back" aria-label="Business card back">
  <svg class="back__waves" viewBox="0 0 710 420" preserveAspectRatio="none" aria-hidden="true">
    <path d="M0,232 Q360,222 710,178 L710,420 L0,420 Z" fill="var(--green)"/>
    <path d="M0,244 Q360,234 710,192 L710,420 L0,420 Z" fill="var(--navy)"/>
  </svg>
  <div class="leaf-decor" role="img" aria-label="Faint leaf decoration" style="width:200px;height:230px;"></div>
  <div class="back__mark">
    <span class="brand-dot brand-dot--small" aria-hidden="true"></span>
    <p class="back__initials">KRT</p>
  </div>
  <div class="holder">
    <p class="holder__name">MARISOL VEGA, B.A.</p>
    <p class="holder__title">Asst. Behavior Analyst (BCABA)<br>(Board Certified)</p>
  </div>
  <ul class="contact">
    <li>
      <svg viewBox="0 0 20 20" aria-hidden="true"><rect x="0.5" y="0.5" width="19" height="19" fill="none" stroke="#fff"/><path d="M6 4 L8.5 4 L9.5 7 L8 8.2 Q9.5 11 11.8 12 L13 10.5 L16 11.5 L16 14 Q10 16 5 9 Q4.5 6 6 4 Z" fill="#fff"/></svg>
      786-555-0142
    </li>
    <li>
      <svg viewBox="0 0 20 20" aria-hidden="true"><rect x="0.5" y="0.5" width="19" height="19" fill="none" stroke="#fff"/><circle cx="10" cy="10" r="6" fill="none" stroke="#fff" stroke-width="1.3"/><ellipse cx="10" cy="10" rx="2.6" ry="6" fill="none" stroke="#fff" stroke-width="1.1"/><line x1="4" y1="10" x2="16" y2="10" stroke="#fff" stroke-width="1.1"/></svg>
      vega.m.aba@krtmail.com
    </li>
  </ul>
</section>

</body>
</html>
```